Web Design for Harbor Ledger Allies

Harbor Ledger Allies needs the photoshop files for a simple, clean and professional website design. The company is building a network of bookkeepers/accountants to handle outsourced bookkeeping services for start ups and small businesses. It needs to both attract bookkeepers to become partners and give clients confidence in the professional network. The partners will use products like Tallymint Web, Brightfolio.example and PennyTrim.example for start ups, as well as help with tasks using the clients existing accounting software.

A home and subpage design is needed. I'll award the work based on the home design. The minor subpage changes can be worked out in the workroom stage.

The pages for the navigation will be: Home, Services, Locations, Partners, FAQ, Contact

```html
<!DOCTYPE html>
<html lang="en">
<head>
<meta charset="utf-8">
<title>Harbor Ledger Allies</title>
<link href="https://fonts.googleapis.com/css2?family=Roboto+Condensed:wght@400;700&family=Arimo:wght@400;700&display=swap" rel="stylesheet">
<style>
:root{
  --blue:#1ea3e0;
  --ink:#333;
  --grey:#6a6a6a;
  --light:#e9e9e9;
  --band:#e2e2e2;
  --dark:#141414;
  --paper:#fdfdfd;
}
*{box-sizing:border-box;margin:0;padding:0}
html,body{width:865px;height:1200px;overflow:hidden;background:var(--paper);font-family:Arimo,Arial,sans-serif;color:var(--ink)}
.page{position:relative;width:865px;height:1200px}
.abs{position:absolute}
.topbar{left:0;top:0;width:865px;height:15px;background:var(--dark);border-bottom:3px solid var(--blue)}
.brand{font-family:Arimo,Arial,sans-serif;font-weight:400;color:var(--grey);font-size:16px;line-height:14.3px;letter-spacing:.3px;text-transform:uppercase}
.brand-mark{display:inline-block;width:12px;height:12px;background:var(--blue);border-radius:50%;margin-right:9px;margin-top:15px;flex:none}
.header-brand{left:104px;top:51px;display:flex}
.main-nav{left:369px;top:78px;width:419px;display:flex;justify-content:space-between;font-family:"Roboto Condensed",sans-serif;font-weight:700;font-size:15px;color:var(--ink)}
.main-nav .sep{color:var(--blue);font-weight:400}
.hero{left:104px;top:113px;width:688px;height:312px;background:linear-gradient(100deg,#d9dbdd 0%,#9ea2a6 35%,#6f7378 60%,#8d9094 100%)}
.hero-title{left:632px;top:157px;border-left:1.5px solid #fff;padding-left:10px;color:#fff;font-family:Arimo,Arial,sans-serif;font-size:21px;line-height:18.5px;text-transform:uppercase}
.dots{left:699px;top:411px;display:flex;gap:6px}
.dots i{display:block;width:16px;height:3px;background:#fff}
.dots i:first-child{background:var(--blue)}
h2{font-family:Arimo,Arial,sans-serif;font-weight:700;font-size:17px;color:#444;text-transform:uppercase;letter-spacing:.1px}
h2 em{font-style:normal;color:var(--blue)}
.section p{font-size:9.2px;line-height:13.2px;color:#333;margin-top:14px}
.more{font-family:"Roboto Condensed",sans-serif;font-weight:700;font-size:10.5px;color:#333;margin-top:14px;display:flex;align-items:center;gap:8px}
.more b{color:var(--blue);font-size:12px;letter-spacing:-2px}
.head{display:flex;align-items:flex-end;gap:6px}
.services{left:106px;top:466px;width:210px}
.partners{left:341px;top:472px;width:210px}
.divider{left:104px;top:661px;width:454px;height:3px;border-top:1px dotted #bbb;border-bottom:1px dotted #bbb}
.locations{left:104px;top:688px;width:442px}
.locations p{margin-top:13px}
.contact{left:575px;top:473px;width:217px;height:301px;background:var(--light);border:2px solid #dcdcdc;text-align:center;padding-top:16px}
.contact h3{font-family:Arimo,Arial,sans-serif;font-weight:700;font-size:18.5px;color:#444}
.contact .sub{font-family:"Roboto Condensed",sans-serif;font-size:14px;color:var(--blue);margin-top:1px}
.field{display:block;width:174px;height:24px;margin:10px auto 0;background:#fff;border:1px solid #d5d5d5;font-size:8px;color:#666;text-align:left;padding:7px 9px}
.field+.field{margin-top:5px}
.field.msg{height:60px;margin-top:6px}
.field sup{color:#e02020;vertical-align:baseline}
.submit{display:block;width:116px;height:27px;margin:12px auto 0;background:linear-gradient(#4ec2f5,#1a9ad6);border:1px solid #168ac2;color:#fff;font-family:"Roboto Condensed",sans-serif;font-weight:700;font-size:13px;line-height:25px}
.sw-band{top:860px;height:21px;background:var(--band)}
.sw-title{left:355px;top:857px;width:186px;text-align:center;font-family:"Roboto Condensed",sans-serif;font-weight:700;font-size:20px;color:#444}
.sw-name{top:935px;width:170px;margin-left:-85px;text-align:center;font-family:Arimo,Arial,sans-serif;font-size:19px;color:#555}
.footer{left:0;top:1058px;width:865px;height:142px;background:var(--dark);border-top:3px solid var(--blue)}
.footer-brand{left:84px;top:1092px;display:flex}
.footer-brand .brand{color:#8a8a8a}
.footer-rule{left:274px;top:1094px;width:1px;height:36px;background:#555}
.footer-nav{left:296px;top:1094px;font-size:9.5px;color:#ddd;display:flex}
.footer-nav .sep{color:var(--blue);margin:0 12px}
.copy{left:296px;top:1121px;font-size:8.8px;color:#ddd}
</style>
</head>
<body>
<div class="page">
  <div class="abs topbar"></div>

  <header class="abs header-brand"><span class="brand-mark"></span><div class="brand">Harbor<br>Ledger<br>Allies</div></header>
  <nav class="abs main-nav"><span>HOME</span><span class="sep">|</span><span>SERVICES</span><span class="sep">|</span><span>LOCATIONS</span><span class="sep">|</span><span>PARTNERS</span><span class="sep">|</span><span>FAQ</span><span class="sep">|</span><span>CONTACT</span></nav>

  <div class="abs hero" role="img" aria-label="Businessman in a grey suit touching a cloud icon connected to devices"></div>
  <div class="abs hero-title">Harbor<br>Ledger<br>Allies</div>
  <div class="abs dots"><i></i><i></i><i></i><i></i></div>

  <section class="abs section services">
    <div class="head">
      <svg width="36" height="36" viewBox="0 0 36 36"><circle cx="13" cy="23" r="8" fill="none" stroke="#666" stroke-width="5" stroke-dasharray="3 2"/><circle cx="13" cy="23" r="3" fill="#666"/><circle cx="28" cy="8" r="5" fill="none" stroke="var(--blue)" stroke-width="3"/></svg>
      <h2>Our <em>Services</em></h2>
    </div>
    <p>Lorem ipsum dolor sit amet, consectetur adipiscing elit. Mauris fringilla nibh vel neque fringilla, quis mattis lorem condimentum. Etiam rhoncus faucibus eros ut egestas. Nulla nulla est, congue in semper vitae, blandit eget mi. Nam posuere laoreet eros in luctus. Vivamus pharetra justo ac risus hendrerit sodales.</p>
    <div class="more"><b>&gt;&gt;</b>VIEW &nbsp;MORE</div>
  </section>

  <section class="abs section partners">
    <div class="head">
      <svg width="36" height="30" viewBox="0 0 36 30"><circle cx="8" cy="8" r="4" fill="#555"/><circle cx="28" cy="8" r="4" fill="#555"/><path d="M1 24a7 7 0 0 1 14 0z M21 24a7 7 0 0 1 14 0z" fill="#555"/><circle cx="18" cy="12" r="5" fill="var(--blue)"/><path d="M9 30a9 9 0 0 1 18 0z" fill="var(--blue)"/></svg>
      <h2>Our <em>Partners</em></h2>
    </div>
    <p>Lorem ipsum dolor sit amet, consectetur adipiscing elit. Mauris fringilla nibh vel neque fringilla, quis mattis lorem condimentum. Etiam rhoncus faucibus eros ut egestas. Nulla nulla est, congue in semper vitae, blandit eget mi. Nam posuere laoreet eros in luctus. Vivamus pharetra justo ac risus hendrerit sodales.</p>
    <div class="more"><b>&gt;&gt;</b>VIEW &nbsp;MORE</div>
  </section>

  <div class="abs divider"></div>

  <section class="abs section locations">
    <div class="head">
      <svg width="14" height="22" viewBox="0 0 14 22"><path d="M7 0a7 7 0 0 1 7 7c0 5-7 15-7 15S0 12 0 7a7 7 0 0 1 7-7z" fill="#666"/><circle cx="7" cy="7" r="2.6" fill="#fff"/></svg>
      <h2>Find <em>Locations</em></h2>
    </div>
    <p>Lorem ipsum dolor sit amet, consectetur adipiscing elit. Mauris fringilla nibh vel neque fringilla, quis mattis lorem condimentum. Etiam rhoncus faucibus eros ut egestas. Nulla nulla est, congue in semper vitae, blandit eget mi. Nam posuere laoreet eros in luctus. Vivamus pharetra justo ac risus hendrerit sodales.</p>
    <div class="more"><b>&gt;&gt;</b>VIEW &nbsp;MORE</div>
  </section>

  <aside class="abs contact">
    <h3>CONTACT US</h3>
    <div class="sub">FOR FREE CONSULTATION</div>
    <div class="field">Name :<sup>*</sup></div>
    <div class="field">Email :<sup>*</sup></div>
    <div class="field">Phone :</div>
    <div class="field">City State :</div>
    <div class="field msg">Message :</div>
    <div class="submit">SUBMIT</div>
  </aside>

  <div class="abs sw-band" style="left:104px;width:251px"></div>
  <div class="abs sw-band" style="left:541px;width:251px"></div>
  <h2 class="abs sw-title">SOFTWARE WE USE</h2>
  <div class="abs sw-name" style="left:192px">Brightfolio</div>
  <div class="abs sw-name" style="left:372px">PennyTrim</div>
  <div class="abs sw-name" style="left:519px">Nimbook</div>
  <div class="abs sw-name" style="left:675px">Tallymint Web</div>

  <footer class="abs footer"></footer>
  <div class="abs footer-brand"><span class="brand-mark"></span><div class="brand">Harbor<br>Ledger<br>Allies</div></div>
  <div class="abs footer-rule"></div>
  <nav class="abs footer-nav">HOME<span class="sep">|</span>SERVICES<span class="sep">|</span>LOCATIONS<span class="sep">|</span>PARTNERS<span class="sep">|</span>FAQ<span class="sep">|</span>CONTACT</nav>
  <div class="abs copy">© 2014 HARBOR LEDGER ALLIES. ALL RIGHTS RESERVED.</div>
</div>
</body>
</html>
```